Small business services company needs a flyer designed

We need a flyer designed for a small building services company who has multiple roles ie- Roof, gutter and pressure cleaning, small building maintenance and garden cleanups. The company is based in Far North Queensland (Australia) where it is a tropical climate with lots of trees and green areas.

I want the colours to be based on the Logo and business card colours which will be added.

The flyer will need to be changeable so I can create monthly specials ie- Roof Cleaning Special, Gutter Cleaning Special or Pressure Cleaning special.

The roles of the business will be as stated on the attached business card.
Updates

Good evening all designers, please find below an update for you all, I hope it may answer some questions you have.

'd like the flyer to be DL size and at present I don't have any photo's. But i'd be happy for you to source some from google. The pictures I'd like would be of gutter cleaning from a ladder, pressure washing roofs & driveways with the large round "flat surface cleaners". Possibly have split pictures of the pressure cleaning to show before and after. 
Far North Queensland is a very tropical environment that has lots of palm trees and rain forest. The climate is usually 30+ degrees C. Incorporating those colours with the logo colours I'd like. 

Hello all designers.

I have just uploaded some of my own job pictures. There is a before and an after picture. If you source any other pictures, I'd like to see a flat surface/ spindeck cleaner in operation, either on a roof or a driveway.

My goal is for a single sided flyer with all the details from my business card to be on the flyer. 

Please remember the climate in my area is very tropical and usually 30+ degrees C. Never cold or snowing. So please have pictures to reflect.

Thanks for the designs.
Regards,Glenn

Reason: hi all designers. I have extended the deadline by 3 days to accommodate all the designers who have only recently accepted the craft hive invites. I have had a lot of declines and want the best designs I can choice from. This is no reflection of the calibre of the designs I have already received. I look forward to seeing all the updates and new designs. Regards, Glenn

Target Market(s)

Home owners who take pride in the street appeal of their homes, or to add value to their selling price when a house goes on the sales market.

Industry/Entity Type

Building

```html
<!DOCTYPE html>
<html lang="en">
<head>
<meta charset="utf-8">
<title>HighReach Flyer</title>
<link href="https://fonts.googleapis.com/css2?family=Open+Sans:wght@400;600;700;800&display=swap" rel="stylesheet">
<style>
  :root{
    --teal:#1aa3a8;
    --teal-light:#3cc0bf;
    --navy:#17326b;
    --blue:#1f5fb3;
    --paper-top:#ffffff;
    --paper-bottom:#dcdde0;
    --stage:#e9eaec;
    --ink:#1d2b55;
  }
  *{box-sizing:border-box;margin:0;padding:0}
  html,body{width:807px;height:1200px;overflow:hidden;background:var(--stage)}
  body{font-family:"Open Sans",Arial,sans-serif;position:relative}
  .flyer{
    position:absolute;left:123px;top:20px;width:560px;height:1160px;
    background:linear-gradient(180deg,var(--paper-top) 55%,var(--paper-bottom) 100%);
    overflow:hidden;box-shadow:0 4px 18px rgba(0,0,0,.18);
  }
  .hero-photo{
    position:absolute;left:0;top:0;width:560px;height:640px;
    background:linear-gradient(160deg,#7d8791 0%,#5b4a44 35%,#a3392f 55%,#c9c4b8 80%,#8f8a7f 100%);
  }
  .swoosh{position:absolute;left:0;top:0;width:560px;height:680px}
  .job-photo{
    position:absolute;width:160px;height:160px;border-radius:50%;
    border:6px solid #fff;box-shadow:0 2px 8px rgba(0,0,0,.3);
  }
  .job-photo.wash{left:28px;top:500px;background:radial-gradient(circle,#c9b89a,#8b7c64)}
  .job-photo.before-after{left:200px;top:520px;background:linear-gradient(90deg,#6f6d66 50%,#b9b6ab 50%)}
  .job-photo.surface{left:378px;top:460px;background:radial-gradient(circle at 55% 45%,#e0c04a,#8e8470 60%)}
  .content{position:absolute;left:44px;top:700px;right:30px}
  .section-title{font-weight:800;font-size:36px;color:var(--teal);letter-spacing:.5px}
  .specialities{list-style:none;margin-top:8px}
  .specialities li{font-size:19px;font-weight:600;color:var(--ink);line-height:1.45;padding-left:28px;position:relative}
  .specialities li::before{content:"\2731";position:absolute;left:0;top:0;color:var(--teal);font-size:17px}
  .job-types{margin-top:20px;text-align:center;font-weight:700;font-size:19px;color:var(--teal)}
  .certification{text-align:center;font-weight:800;font-size:19px;color:var(--navy);margin-top:2px}
  .offer{margin-top:22px;text-align:center}
  .offer-title{font-weight:800;font-size:34px;color:var(--teal)}
  .offer-note{font-size:19px;color:var(--ink);font-weight:600}
  .footer{position:absolute;left:40px;right:30px;bottom:30px;display:flex;justify-content:space-between;align-items:flex-end}
  .contact{font-size:15px;color:var(--ink);line-height:1.55;font-weight:600}
  .contact span{display:flex;align-items:center;gap:8px}
  .contact svg{width:14px;height:14px;fill:var(--blue)}
  .contact .abn{padding-left:22px}
  .brand{text-align:right;display:flex;align-items:center;gap:10px}
  .brand-mark{width:34px;height:34px;background:var(--navy)}
  .brand-name{font-weight:800;font-size:32px;color:var(--navy);line-height:1}
  .brand-tag{font-size:9px;color:var(--navy);font-weight:600;margin-top:3px}
</style>
</head>
<body>
<div class="flyer">
  <div class="hero-photo" role="img" aria-label="Worker on a ladder cleaning a house gutter"></div>
  <svg class="swoosh" viewBox="0 0 560 680" aria-hidden="true">
    <path d="M560 170 C 470 420, 300 600, 0 650 L0 680 L560 680 Z" fill="#ffffff"/>
    <path d="M560 210 C 480 430, 320 590, 40 640 C 330 610, 520 450, 560 330 Z" fill="var(--blue)"/>
    <path d="M560 130 C 470 380, 320 560, 60 630 C 320 580, 500 420, 560 240 Z" fill="var(--teal-light)"/>
  </svg>
  <div class="job-photo wash" role="img" aria-label="Pressure cleaning a paved area"></div>
  <div class="job-photo before-after" role="img" aria-label="Before and after driveway cleaning"></div>
  <div class="job-photo surface" role="img" aria-label="Flat surface cleaner on a driveway"></div>

  <div class="content">
    <h2 class="section-title">SPECIALITIES:</h2>
    <ul class="specialities">
      <li>Gutter Cleaning</li>
      <li>Pressure Cleaning-Roof's, Driveways etc</li>
      <li>Minor Roof, Gutter &amp; Building Maintenance</li>
      <li>Garden Waste Removal &amp; Complex Cleanups</li>
    </ul>
    <p class="job-types">Residential, Commercial &amp; Body Corporate Jobs</p>
    <p class="certification">National Working at Heights Certification</p>
    <div class="offer">
      <p class="offer-title">10% DISCOUNT</p>
      <p class="offer-note">for Emergency Services, Defence &amp; Seniors</p>
    </div>
  </div>

  <div class="footer">
    <div class="contact">
      <span><svg viewBox="0 0 24 24"><path d="M6.6 10.8a15 15 0 0 0 6.6 6.6l2.2-2.2a1 1 0 0 1 1-.25 11.4 11.4 0 0 0 3.6.57 1 1 0 0 1 1 1V20a1 1 0 0 1-1 1A17 17 0 0 1 3 4a1 1 0 0 1 1-1h3.5a1 1 0 0 1 1 1c0 1.25.2 2.45.57 3.6a1 1 0 0 1-.25 1z"/></svg>0400 555 012</span>
      <span><svg viewBox="0 0 24 24"><path d="M2 5h20v14H2z M2 5l10 8 10-8" fill="none" stroke="#1f5fb3" stroke-width="2.4"/></svg>jobs@highreachclean.au</span>
      <span class="abn">ABN - 12 345 678 901</span>
    </div>
    <div class="brand">
      <div class="brand-mark"></div>
      <div>
        <p class="brand-name">HIGHREACH</p>
        <p class="brand-tag">Roof, Gutter &amp; Pressure Cleaning</p>
      </div>
    </div>
  </div>
</div>
</body>
</html>
```